Letterhead needed using basic elements of our new logo!

We have just had a new logo and business card created on Pixel Harbor and now would like a new letterhead for our company re-branding. Our logo inspires trust, professionalism and confidence and we would like to mirror that in our letterhead. We would like to use elements in our logo (as well as the logo itself, obviously), but understand with only a header and the ability to print in black and white, we are somewhat limited. We have also won the Resident's Pick Medal for best Property Management Company in our city and would like to somehow include that small banner (see uploaded file) in the letterhead, without it clashing?

Text to include:
Stonebrook Property Management (and logo)
C-214 Marlowe Ave, Winnipeg, MB R2K 3P7
Ph: 204-738-2915
Fax: 1-888-276-9413
Email: customerservice@stonebrookpropertymanagement.example
Web: www.stonebrookpropertymanagement.example

Pasted below is our mission, vision and branding statements to help with the project:

Mission Statement

Provide the highest quality customer service to both property owners and tenants using innovative technology and well trained, caring staff.

Vision Statement

To redefine the way in which management is delivered to its customers, becoming the recognized leader in the property management industry.

Brand Essence

When our customers experience our product or service, it brings forth an emotion of absolute trust that we have their best interests at heart

Brand Personality

We are a company that is passionate about our customers, our company and our vision to be leaders in the field of property management. We are visionaries that aren't afraid to use cutting edge technologies to improve our products and service.

Position or Value Proposition

To whom are we speaking?
- real estate investors, including first timers that are giving us their first starter home. They are fairly naive, as they are not "big time" investors, and because they are giving us their first home (in contract to an investor buying a rental property, often sight unseen) they are more emotionally tied to their property and will require a company that inspires trust and confidence.

What is our brand promise?
- we will do our best to serve our clients, both owners and tenants, to give them prompt communication, clear, concise answers to their questions, and look after their property quickly and competently.

Why is our product different than the competition and why should our customers care?
- the current model used by most management companies employs individual portfolio managers that do things a little differently each instance, and differently than their fellow staff members. Our management product is superior because we use a combination of technology and strict procedures to ensure each client's experience is consistent, each and every time.

Industry/Entity Type

Business

Requirements
Must have
• We would like an option to be in black and white, to be able to be printed from Microsoft Word. As well, we do not want anything in a footer or any other kind of letterhead that bleeds below a header. The main use of this letterhead will be from our property management software, to be used in our form letters and other templates (sent to tenants and clients)
Should not have
• Footer or other elements where the text body would be, it will be used in a form letter

```html
<!DOCTYPE html>
<html lang="en">
<head>
<meta charset="utf-8">
<title>Stonebrook Property Management Letterhead</title>
<link href="https://fonts.googleapis.com/css2?family=PT+Sans:wght@400;700&family=Roboto:wght@500;700&display=swap" rel="stylesheet">
<style>
  :root {
    --backdrop: #dccbb4;
    --paper: #ffffff;
    --brand-blue: #1b8fd6;
    --ink: #3a3a3a;
    --body-grey: #7d7d7d;
    --medal-gold: #d9a520;
    --signature-fill: #ececec;
  }
  * { margin: 0; padding: 0; box-sizing: border-box; }
  html, body { width: 1200px; height: 1200px; overflow: hidden; }
  body { background: var(--backdrop); position: relative; font-family: "PT Sans", Arial, sans-serif; }

  .letterhead {
    position: absolute; left: 176px; top: 0;
    width: 848px; height: 1200px;
    background: var(--paper);
    color: var(--ink);
  }

  .brand { position: absolute; left: 119px; top: 84px; display: flex; align-items: center; gap: 12px; }
  .brand-mark { width: 40px; height: 40px; background: var(--brand-blue); }
  .brand-name { font-family: "Roboto", Arial, sans-serif; font-weight: 700; font-size: 22px; color: var(--brand-blue); letter-spacing: 0.3px; }

  .address { position: absolute; right: 130px; top: 88px; text-align: right; font-style: normal; font-size: 14px; line-height: 17.5px; color: var(--ink); }
  .contact { position: absolute; right: 130px; top: 150px; text-align: right; font-size: 11.5px; line-height: 15px; color: var(--ink); }
  .contact b { color: var(--brand-blue); font-weight: 700; }

  .recipient { position: absolute; left: 121px; top: 226px; }
  .recipient .salutation { font-family: "Roboto", Arial, sans-serif; font-weight: 700; font-size: 14px; }
  .recipient .salutation span { display: inline-block; width: 82px; border-bottom: 1px solid var(--ink); }
  .recipient .designation { font-size: 10.5px; line-height: 14px; }
  .recipient .company { font-size: 10.5px; font-weight: 700; }
  .date { position: absolute; right: 128px; top: 226px; font-family: "Roboto", Arial, sans-serif; font-weight: 700; font-size: 14px; letter-spacing: 0.3px; }

  .statements { position: absolute; left: 121px; top: 302px; width: 600px; }
  .statement { margin-bottom: 13px; }
  .statement h2 { font-family: "Roboto", Arial, sans-serif; font-weight: 700; font-size: 17px; letter-spacing: 0.8px; color: var(--ink); margin-bottom: 3px; }
  .statement h3 { font-family: "Roboto", Arial, sans-serif; font-weight: 700; font-size: 14px; letter-spacing: 0.5px; color: var(--ink); margin-top: 1px; }
  .statement h3.plain { font-family: "PT Sans", Arial, sans-serif; font-size: 14.5px; letter-spacing: 0; }
  .statement p { font-size: 14px; line-height: 17.2px; color: var(--body-grey); }

  .sign-block { position: absolute; left: 121px; top: 965px; }
  .sign-block .name { font-family: "Roboto", Arial, sans-serif; font-weight: 700; font-size: 17px; letter-spacing: 1px; }
  .sign-block .role { font-size: 13.5px; margin-top: 1px; }
  .signature { width: 142px; height: 40px; margin-top: 10px; background: var(--signature-fill); }
  .signature-rule { width: 143px; height: 3px; background: var(--ink); margin-top: 2px; }

  .medal { position: absolute; left: 606px; top: 952px; width: 108px; height: 108px; border-radius: 50%; background: var(--medal-gold); }
</style>
</head>
<body>
<div class="letterhead">
  <div class="brand">
    <div class="brand-mark"></div>
    <div class="brand-name">Stonebrook Property Management</div>
  </div>

  <address class="address">
    C-214 Marlowe Ave,<br>Winnipeg, MB<br>R2K 3P7
  </address>
  <div class="contact">
    <div><b>Ph:</b> 204-738-2915 &nbsp; <b>Fax:</b> 1-888-276-9413</div>
    <div>customerservice@stonebrookpropertymanagement.example</div>
    <div>www.stonebrookpropertymanagement.example</div>
  </div>

  <div class="recipient">
    <div class="salutation">Dear, Mr<span>&nbsp;</span></div>
    <div class="designation">Designation</div>
    <div class="company">COMPANY NAME</div>
  </div>
  <div class="date">DATE:1/8/2018</div>

  <div class="statements">
    <section class="statement">
      <h2>Mission Statement</h2>
      <p>Provide the highest quality customer service to both property owners and tenants using innovative technology and well trained, caring staff.</p>
    </section>
    <section class="statement">
      <h2>Vision Statement</h2>
      <p>To redefine the way in which management is delivered to its customers, becoming the recognized leader in the property management industry.</p>
    </section>
    <section class="statement">
      <h2>Brand Essence</h2>
      <p>When our customers experience our product or service, it brings forth an emotion of absolute trust that we have their best interests at heart</p>
    </section>
    <section class="statement">
      <h2>Brand Personality</h2>
      <p>We are a company that is passionate about our customers, our company and our vision to be leaders in the field of property management. We are visionaries that aren't afraid to use cutting edge technologies to improve our products and service.</p>
    </section>
    <section class="statement">
      <h2>Position or Value Proposition</h2>
      <h3>To whom are we speaking?</h3>
      <p>real estate investors, including first timers that are giving us their first starter home. They are fairly naive, as they are not "big time" investors,and because they are giving us their first home (in contract to an investor buying a rental property, often sight unseen) they are more emotionally tied to their property and will require a company that inspires trust and confidence.</p>
    </section>
    <section class="statement">
      <h3>What is our brand promise?</h3>
      <p>we will do our best to serve our clients, both owners and tenants, to give them prompt communication, clear, concise answers to their questions, and look after their property quickly and competently.</p>
    </section>
    <section class="statement">
      <h3 class="plain">Why is our product different than the competition and why should our customers care?</h3>
      <p>the current model used by most management companies employs individual portfolio managers that do things a little differently each instance, and differently than their fellow staff members. Our management product is superior because we use a combination of technology and strict procedures to ensure each client's experience is consistent, each and every time.</p>
    </section>
  </div>

  <div class="sign-block">
    <div class="name">YOUR NAME</div>
    <div class="role">Designation</div>
    <div class="signature" role="img" aria-label="Handwritten signature"></div>
    <div class="signature-rule"></div>
  </div>

  <div class="medal" role="img" aria-label="Resident's Pick Medal badge"></div>
</div>
</body>
</html>
```